Prominent Law Firm Needs a New Stationary Design

We need new stationary design to go with our new logo and rustic offices.
Things we need on the letterhead:
logo (see attached file), would also like the Seven-Figure Verdict Logo (attached) somewhere on the stationary,
5182 North Pelham Avenue
Tulsa, Oklahoma 74219
(918) 555-0143 Tel ★ (918) 555-0187 Fax
www.TWVQX.example

We also need the names of the 4 partners:
Dale K. Hollingsworth
Vernon P. Hollingsworth
Mark E. Fenwicke
Tyler D. Ashcombe

And the other staff:
Brenda K. Lyle
Tendaji K. Oyelowanta
Gordon Pettijo

Hilda V. Pruitt, RN

Of Counsel:
Wendell S. Hollingsworth

Industry/Entity Type

Law Firm

```html
<!DOCTYPE html>
<html lang="en">
<head>
<meta charset="utf-8">
<title>Hollingsworth Hollingsworth Fenwicke Letterhead</title>
<link rel="stylesheet" href="https://fonts.googleapis.com/css2?family=Tinos&display=swap">
<style>
  :root {
    --backdrop: #e8e9eb;
    --paper: #ffffff;
    --maroon: #581215;
    --label: #b4676d;
    --ink: #3b0b0e;
    --logo-ink: #c98a8f;
    --rule: #c2868b;
  }
  * { margin: 0; padding: 0; box-sizing: border-box; }
  html, body {
    width: 1178px;
    height: 1200px;
    overflow: hidden;
    background: var(--backdrop);
  }
  .letterhead {
    position: absolute;
    left: 139px;
    top: 24px;
    width: 900px;
    height: 1152px;
    background: var(--paper);
    font-family: "Tinos", "Times New Roman", serif;
    color: var(--ink);
  }
  .brand-block {
    position: absolute;
    left: 15px;
    top: 14px;
    width: 288px;
    height: 218px;
    background: var(--maroon);
    display: flex;
    flex-direction: column;
    align-items: center;
    justify-content: center;
    text-align: center;
    color: var(--logo-ink);
    font-size: 22px;
    line-height: 30px;
    letter-spacing: 1px;
  }
  .sidebar {
    position: absolute;
    left: 0;
    top: 257px;
    width: 231px;
    height: 863px;
    border-right: 1.5px solid var(--rule);
    padding-right: 10px;
    text-align: right;
    font-size: 17.5px;
    line-height: 22px;
  }
  .roster-group { margin-bottom: 22px; }
  .roster-label { color: var(--label); text-transform: uppercase; }
  .contact {
    position: absolute;
    right: 10px;
    bottom: 0;
  }
  .contact .tag { color: var(--label); }
  .contact .web-accent { color: var(--label); }
</style>
</head>
<body>
  <main class="letterhead">
    <div class="brand-block">
      <span>Hollingsworth</span>
      <span>Hollingsworth</span>
      <span>Fenwicke</span>
    </div>

    <aside class="sidebar">
      <section class="roster-group">
        <p class="roster-label">Partners</p>
        <p>Dale K. Hollingsworth</p>
        <p>Vernon P. Hollingsworth</p>
        <p>Mark E. Fenwicke</p>
        <p>Tyler D. Ashcombe</p>
      </section>
      <section class="roster-group">
        <p class="roster-label">Other Staffs</p>
        <p>Brenda K. Lyle</p>
        <p>Tendaji K. Oyelowanta</p>
        <p>Gordon Pettijo</p>
      </section>
      <section class="roster-group">
        <p>Hilda V. Pruitt, RN</p>
      </section>
      <section class="roster-group">
        <p class="roster-label">Of Counsel</p>
        <p>Wendell S. Hollingsworth</p>
      </section>

      <address class="contact" style="font-style: normal;">
        <p>5182 North Pelham Avenue</p>
        <p>Tulsa, Oklahoma 74219</p>
        <p><span class="tag">Tel</span> (918) 555-0143</p>
        <p><span class="tag">Fax</span> (918) 555-0187</p>
        <p>www.<span class="web-accent">TWVQX</span>.example</p>
      </address>
    </aside>
  </main>
</body>
</html>
```